Company director needs a business card design

I am a semi-retired former senior finance executive who sits on a number of public and private company boards and do some consulting work. I work largely with emerging businesses but deal regularly with top end of town lawyers, bankers etc. I need a thoughtful but relatively conservative design which would also resonate with my younger client base. Some colour would be good. Information limited to name, address, office tel, mobile and email.

Industry/Entity Type

Finance

```html
<!DOCTYPE html>
<html lang="en">
<head>
<meta charset="utf-8">
<title>Daniel Whitford – Business Card</title>
<link rel="stylesheet" href="https://fonts.googleapis.com/css2?family=Quicksand:wght@500;600&display=swap">
<style>
  :root {
    --backdrop: #2b2b2d;
    --card-white: #ffffff;
    --ink-black: #1d1b1c;
    --panel-black: #231f20;
  }
  * { margin: 0; padding: 0; box-sizing: border-box; }
  html, body {
    width: 1200px;
    height: 801px;
    overflow: hidden;
    background: var(--backdrop);
  }
  .stage {
    position: relative;
    width: 1200px;
    height: 801px;
  }
  .card {
    position: absolute;
    left: 110px;
    top: 120px;
    width: 980px;
    height: 560px;
    background: var(--card-white);
    overflow: hidden;
    font-family: "Quicksand", "Varela Round", sans-serif;
    color: var(--ink-black);
  }
  .card__panel {
    position: absolute;
    inset: 0;
    width: 980px;
    height: 560px;
  }
  .contact-line {
    position: absolute;
    font-size: 30px;
    font-weight: 600;
    white-space: nowrap;
    letter-spacing: -0.2px;
  }
  .contact-icon {
    position: absolute;
    width: 46px;
    height: 46px;
  }
  .contact-line--address { left: 140px; top: 140px; }
  .contact-line--email   { left: 288px; top: 240px; }
  .contact-line--office  { left: 438px; top: 340px; }
  .contact-line--mobile  { left: 580px; top: 436px; }
  .contact-icon--pin    { left: 52px;  top: 140px; }
  .contact-icon--mail   { left: 185px; top: 238px; }
  .contact-icon--office { left: 340px; top: 338px; }
  .contact-icon--mobile { left: 480px; top: 432px; }
  .holder-name {
    position: absolute;
    left: 52px;
    top: 400px;
    color: var(--card-white);
    font-size: 48px;
    font-weight: 600;
    line-height: 56px;
  }
  .holder-rule {
    position: absolute;
    left: 36px;
    top: 522px;
    width: 340px;
    height: 16px;
    background: var(--card-white);
  }
</style>
</head>
<body>
<main class="stage">
  <section class="card" aria-label="Business card of Daniel Whitford">
    <svg class="card__panel" viewBox="0 0 980 560" aria-hidden="true">
      <polygon points="0,90 0,560 700,560" fill="var(--panel-black)"/>
    </svg>

    <svg class="contact-icon contact-icon--pin" viewBox="0 0 46 46" aria-hidden="true">
      <path d="M23 3c-8 0-14 6-14 14 0 10 14 26 14 26s14-16 14-26c0-8-6-14-14-14z" fill="#fff"/>
      <circle cx="23" cy="17" r="5.5" fill="var(--panel-black)"/>
    </svg>
    <p class="contact-line contact-line--address">18 Larkspur Street, Seaview NSW 2099</p>

    <svg class="contact-icon contact-icon--mail" viewBox="0 0 46 46" aria-hidden="true">
      <path d="M4 18 L23 6 L42 18 V40 H4 Z" fill="#fff"/>
      <path d="M4 18 L23 30 L42 18" fill="none" stroke="var(--panel-black)" stroke-width="2"/>
      <path d="M14 20 h18 M15 24 h16" stroke="var(--panel-black)" stroke-width="2"/>
    </svg>
    <p class="contact-line contact-line--email">daniel_whitford@mailnet.net.au</p>

    <svg class="contact-icon contact-icon--office" viewBox="0 0 46 46" aria-hidden="true">
      <path d="M18 14c-3 2-4 6-2 10 4 8 10 13 17 15 3 1 6 0 7-3l-5-5-4 2c-4-2-7-6-8-10l3-3z" fill="#fff" transform="rotate(-10 23 23)"/>
      <path d="M12 6c-5 4-7 10-5 16 M7 4c-6 6-8 13-5 20" fill="none" stroke="#fff" stroke-width="2.4" stroke-linecap="round"/>
    </svg>
    <p class="contact-line contact-line--office">02 9451 2860</p>

    <svg class="contact-icon contact-icon--mobile" viewBox="0 0 46 46" aria-hidden="true">
      <rect x="16" y="8" width="20" height="36" rx="4" fill="#fff"/>
      <rect x="19" y="12" width="14" height="10" rx="1" fill="var(--panel-black)"/>
      <g fill="var(--panel-black)">
        <circle cx="21" cy="27" r="1.5"/><circle cx="26" cy="27" r="1.5"/><circle cx="31" cy="27" r="1.5"/>
        <circle cx="21" cy="32" r="1.5"/><circle cx="26" cy="32" r="1.5"/><circle cx="31" cy="32" r="1.5"/>
        <circle cx="21" cy="37" r="1.5"/><circle cx="26" cy="37" r="1.5"/><circle cx="31" cy="37" r="1.5"/>
      </g>
      <path d="M11 10c-3 3-3 7 0 10 M7 7c-5 5-5 11 0 16" fill="none" stroke="#fff" stroke-width="2.2" stroke-linecap="round"/>
    </svg>
    <p class="contact-line contact-line--mobile">0412 583 907</p>

    <h1 class="holder-name">Daniel<br>Whitford</h1>
    <div class="holder-rule"></div>
  </section>
</main>
</body>
</html>
```